Residential Construction Business - Site Signage

I need a design made for a site fence banner. We have a logo and branding so the design would need to be aligned with this. It would need to be made to specific size ratio so that it can be sent to the maker for production.
ratio : 4600 wide x 1700 high
The design should feature our website and also the slogan
"don't move, re-imagine"

Target Market(s)

potential clients

Industry/Entity Type

construction

Font styles to use
Other font styles liked:
• to match branding

Colors
0054AA
0677BA
7BADD7
CADEEF
E8F1F8

Requirements
Must have
• www.velmbuild.com.au Majority of the sign is our brand logo
Nice to have
• Majority of the sign is our brand logo
Should not have
• colors and themes that arent brand relevant

```html
<!DOCTYPE html>
<html lang="en">
<head>
<meta charset="utf-8">
<title>Velm Build – Site Fence Banner</title>
<link href="https://fonts.googleapis.com/css2?family=Montserrat:wght@500;600;700&display=swap" rel="stylesheet">
<style>
  :root {
    --brand-navy: #053a5c;
    --banner-white: #ffffff;
    --backdrop: #808080;
  }
  * { margin: 0; padding: 0; box-sizing: border-box; }
  html, body {
    width: 1200px;
    height: 1138px;
    overflow: hidden;
    background: var(--backdrop);
  }
  .banner {
    position: absolute;
    left: 50px;
    top: 366px;
    width: 1100px;
    height: 406px;
    background: var(--banner-white);
    box-shadow: 0 12px 14px rgba(0, 0, 0, 0.28);
    overflow: hidden;
    font-family: "Montserrat", sans-serif;
    color: var(--brand-navy);
  }
  .banner__chevron {
    position: absolute;
    inset: 0;
    width: 1100px;
    height: 406px;
  }
  .banner__chevron path { fill: var(--brand-navy); }
  .brand-name {
    position: absolute;
    left: 290px;
    top: 187px;
    font-size: 42px;
    font-weight: 600;
    letter-spacing: 0.22em;
    line-height: 1;
    white-space: nowrap;
  }
  .divider {
    position: absolute;
    left: 698px;
    top: 105px;
    width: 2px;
    height: 254px;
    background: var(--brand-navy);
  }
  .slogan {
    position: absolute;
    left: 728px;
    top: 156px;
    font-size: 35px;
    font-weight: 700;
    letter-spacing: 0.2em;
    line-height: 33px;
    text-transform: uppercase;
    white-space: nowrap;
  }
  .website {
    position: absolute;
    left: 730px;
    top: 237px;
    font-size: 14.5px;
    font-weight: 500;
    letter-spacing: 0.16em;
    text-transform: uppercase;
    white-space: nowrap;
  }
</style>
</head>
<body>
  <section class="banner" aria-label="Velm Build site fence banner">
    <svg class="banner__chevron" viewBox="0 0 1100 406" aria-hidden="true">
      <path d="M0 0 H429 L272 192 Q263 203 272 214 L443 406 H0 Z"/>
    </svg>
    <div class="brand-name">VELM BUILD</div>
    <div class="divider"></div>
    <p class="slogan">Don’t move<br>re-imagine</p>
    <p class="website">www.velmbuild.com.au</p>
  </section>
</body>
</html>
```